Aviation security consulting company needs a website

We need a website design for Brisk Holloway, and aviation security consulting company. Brisk Holloway (www.briskholloway.example) is an aviation security consulting company that works with government and industry stakeholders in over 60 countries on aviation security strategy, governance, and oversight at the regulatory and operational level.
Brisk Holloway is strongly internationally focused.
The website required should be simple, corporate, serious, and communicate professionalism, reliability and honesty. We are trying to give the company a feeling of being well established.
The attached files include the company logo, along with examples of company web page styles that we like.
The Brisk Holloway website need only be around five pages long (landing page, who we are, our services, our clients, contact), though don't feel limited to only five pages.
The existing website (www.briskholloway.example) was rushed and put together using Wix. We don't love the existing website as it looks too amateur, so don't use it as a template.
There is no requirement for any online sales tools to be included in the site. The site is purely informational, with the option of people making contact via email.

```html
<!DOCTYPE html>
<html lang="en">
<head>
<meta charset="utf-8">
<title>Brisk Holloway – Aviation Security Consulting</title>
<link rel="stylesheet" href="https://fonts.googleapis.com/css2?family=Montserrat:wght@400;500;600&display=swap">
<style>
:root{
  --navy:#14244f;
  --blue:#0b4f8a;
  --button:#1a6fc4;
  --gold:#f2c200;
  --dot-active:#f29b0c;
  --dot:#c8c8c8;
  --text:#4a4a4a;
  --dark:#1c1c1c;
  --muted:#b9b9b9;
  --faint:#f0f0f0;
  --rule:#d6d6d6;
  --bg:#ffffff;
}
*{margin:0;padding:0;box-sizing:border-box}
html,body{width:1200px;height:1200px;overflow:hidden;background:var(--bg)}
body{font-family:"Montserrat",sans-serif;color:var(--text);position:relative}
.abs{position:absolute}

.brand{left:184px;top:26px;display:flex;align-items:center;gap:9px}
.brand-mark{width:47px;height:47px;background:var(--navy)}
.brand-name{font-size:23px;font-weight:600;color:var(--navy);line-height:1;letter-spacing:-.3px}
.brand-tag{font-size:10px;color:var(--navy);letter-spacing:1.6px;margin-top:3px}

.main-nav{top:54px;right:184px;display:flex;gap:19px;font-size:11px;font-weight:500;color:var(--navy);letter-spacing:.4px}

.hero-photo{left:184px;top:97px;width:403px;height:329px;background:linear-gradient(180deg,#cfcfcf 0%,#9a9a9a 35%,#6d6d6d 65%,#8a8a8a 100%)}
.hero-caption{left:184px;top:442px;width:360px;font-size:12px;font-weight:500;color:var(--dark);line-height:17px}
.slider-dots{left:184px;top:487px;display:flex;gap:6px}
.slider-dots span{width:12px;height:12px;border-radius:50%;background:var(--dot)}
.slider-dots span.active{background:var(--dot-active)}

.welcome-card{left:556px;top:176px;width:460px;height:362px;background:#fff;box-shadow:0 2px 14px rgba(0,0,0,.08);padding:31px 37px}
.welcome-card h1{font-size:25.5px;font-weight:500;color:var(--blue);line-height:30px}
.accent{width:108px;height:2px;background:var(--gold);margin:17px 0 18px}
.welcome-card p{font-size:11.5px;line-height:16.8px;margin-bottom:16px}
.btn{display:inline-block;background:var(--button);color:#fff;font-size:12px;font-weight:500;padding:5px 15px;letter-spacing:.3px;margin-top:2px}

.practice-title{left:0;width:1162px;top:580px;text-align:center;font-size:24px;font-weight:500;color:var(--blue)}
.practice-accent{left:526px;top:617px;width:109px;height:2px;background:var(--gold)}
.practice-intro{left:240px;top:639px;width:690px;text-align:center;font-size:11.5px;line-height:16.8px}

.tiles{left:226px;top:718px;display:flex;gap:20px}
.tile{width:124px;height:124px;background:#fff;box-shadow:0 1px 6px rgba(0,0,0,.08);display:flex;flex-direction:column;align-items:center;padding-top:20px;font-size:10.5px;color:#9a9a9a;text-align:center;line-height:13px;letter-spacing:.3px}
.tile.active{box-shadow:0 2px 9px rgba(0,0,0,.2);color:var(--blue);font-weight:500;margin-top:-3px}
.tile svg{width:62px;height:54px;margin-bottom:7px}

.section-faint{font-size:20px;font-weight:500;color:var(--muted)}
.quote-mark{left:226px;top:896px;font-size:150px;color:var(--faint);font-family:Georgia,serif;line-height:1}
.testimonial-title{left:258px;top:926px}
.testimonial-text{left:257px;top:966px;width:290px;font-size:11.5px;line-height:16.8px;color:var(--muted)}
.testimonial-cite{left:258px;top:1034px;font-size:11.5px;font-style:italic;color:var(--muted)}
.clients-title{left:601px;top:926px}
.client-grid{left:602px;top:972px;display:grid;grid-template-columns:repeat(3,118px);row-gap:26px;column-gap:1px}
.client-name{font-size:16px;font-weight:600;color:var(--muted);height:28px;display:flex;align-items:center;white-space:nowrap}

.footer-rule{left:184px;top:1110px;width:832px;height:1px;background:var(--rule)}
.footer-links{left:183px;top:1137px;font-size:10.5px;color:var(--text)}
.footer-links span{margin:0 5px}
.copyright{right:184px;top:1137px;font-size:10.5px;color:var(--text)}
</style>
</head>
<body>

<header>
  <div class="brand abs">
    <div class="brand-mark"></div>
    <div>
      <div class="brand-name">Brisk Holloway</div>
      <div class="brand-tag">aviation security consulting</div>
    </div>
  </div>
  <nav class="main-nav abs">
    <span>WHO WE ARE</span><span>WHAT WE DO</span><span>WHERE WE WORK</span><span>PROJECTS</span><span>LEADERSHIP</span><span>CONTACT</span>
  </nav>
</header>

<section>
  <div class="hero-photo abs" role="img" aria-label="Black and white photo of a passenger jet parked at an airport gate with a tug vehicle"></div>
  <p class="hero-caption abs">Lorem ipsum dolor sit amet, consectetur adipiscing elit, sed do eiusmod tempor incididunt ut labore et dolore</p>
  <div class="slider-dots abs"><span class="active"></span><span></span><span></span><span></span></div>

  <article class="welcome-card abs">
    <h1>Welcome to Brisk Holloway aviation security consulting</h1>
    <div class="accent"></div>
    <p>Brisk Holloway works with government and industry on aviation security regulatory and operational strategy, governance, and oversight.Lorem ipsum dolor sit amet, consectetur adipiscing elit, sed do eiusmod tempor incididunt ut labor exercitation ullamco laboris nisi ut aliquip ex ea commodo consequat.</p>
    <p>Lorem ipsum dolor sit amet, consectetur adipiscing elit, sed do eiusmod tempor incididunt ut labore et dolore magna aliqua. Ut enim ad minim veniam, quis nostrud exercitation.</p>
    <span class="btn">READ MORE</span>
  </article>
</section>

<section>
  <h2 class="practice-title abs">Practice Areas</h2>
  <div class="practice-accent abs"></div>
  <p class="practice-intro abs">Lorem ipsum dolor sit amet, consectetur adipiscing elit, sed do eiusmod tempor incididunt ut labore et dolore magna aliqua. Ut enim ad minim veniam, quis nostrud exercitation ullamco laboris nisi ut aliquip ex ea commodo consequat. Duis aute irure dolor in reprehenderit in voluptate velit esse cillum dolore eu fugiat nulla pariatur.</p>

  <div class="tiles abs">
    <div class="tile active">
      <svg viewBox="0 0 62 54" fill="#222"><path d="M22 8a13 13 0 0 1 18 0" stroke="#222" stroke-width="2.5" fill="none"/><path d="M26 13a7 7 0 0 1 10 0" stroke="#222" stroke-width="2.5" fill="none"/><circle cx="31" cy="18" r="2.5"/><rect x="30" y="21" width="2" height="7"/><ellipse cx="31" cy="38" rx="9" ry="7"/><path d="M3 40 L22 35 L22 41 Z M59 40 L40 35 L40 41 Z"/><rect x="22" y="44" width="3" height="5"/><rect x="37" y="44" width="3" height="5"/></svg>
      REGULATORS
    </div>
    <div class="tile">
      <svg viewBox="0 0 62 54" fill="#222"><path d="M18 18 L46 8 Q52 6 50 10 L26 22 Z"/><path d="M30 12 L24 6 L28 5 L38 10 Z"/><path d="M8 36 h8 v10 h-8 z"/><path d="M16 37 Q26 32 34 36 L44 33 Q50 32 48 36 L38 44 Q28 48 16 46 Z"/></svg>
      CAPACITY<br>DEVELOPMENT
    </div>
    <div class="tile">
      <svg viewBox="0 0 62 54" fill="#222"><rect x="4" y="14" width="16" height="5"/><rect x="10" y="19" width="4" height="29"/><rect x="4" y="47" width="56" height="3"/><rect x="18" y="32" width="42" height="3"/><rect x="26" y="35" width="2" height="12"/><rect x="36" y="35" width="2" height="12"/><rect x="46" y="35" width="2" height="12"/><rect x="56" y="35" width="2" height="12"/><path d="M38 14 L56 6 Q60 5 58 8 L42 16 Z"/></svg>
      AIRPORTS
    </div>
    <div class="tile">
      <svg viewBox="0 0 62 54" fill="#222"><circle cx="16" cy="10" r="7" fill="none" stroke="#222" stroke-width="2"/><path d="M16 6 v4 h3" stroke="#222" stroke-width="2" fill="none"/><circle cx="46" cy="16" r="4"/><path d="M36 48 L40 22 L52 22 L56 48 Z"/><rect x="8" y="32" width="14" height="2"/><rect x="14" y="34" width="2" height="14"/><rect x="30" y="36" width="14" height="4"/></svg>
      AIRLINES
    </div>
    <div class="tile">
      <svg viewBox="0 0 62 54" fill="none" stroke="#222" stroke-width="2.5"><path d="M14 4 L18 6 L26 42"/><circle cx="24" cy="47" r="4"/><path d="M26 42 L52 34"/><rect x="26" y="18" width="18" height="14" transform="rotate(-15 35 25)"/><rect x="28" y="8" width="12" height="10" transform="rotate(-15 34 13)"/></svg>
      AIR CARGO
    </div>
  </div>
</section>

<section>
  <div class="quote-mark abs" aria-hidden="true">“</div>
  <h3 class="section-faint testimonial-title abs">What our Clients say</h3>
  <p class="testimonial-text abs">“Lorem ipsum dolor sit amet, consectetur adipiscing elit, sed do eiusmod tempor incididunt ut labore et dolore magna aliqua. ”</p>
  <p class="testimonial-cite abs">-Client Quotes</p>

  <h3 class="section-faint clients-title abs">Our Clients</h3>
  <div class="client-grid abs">
    <span class="client-name">Skyvane</span>
    <span class="client-name">Norrell Air</span>
    <span class="client-name">Veltaro</span>
    <span class="client-name">Quillara</span>
    <span class="client-name">Tessaro Air</span>
    <span class="client-name">Kestrel Bay</span>
  </div>
</section>

<footer>
  <div class="footer-rule abs"></div>
  <div class="footer-links abs">Home<span>|</span>About<span>|</span>Contact Us</div>
  <div class="copyright abs">© 2016 Brisk Holloway. All Rights Reserved.</div>
</footer>

</body>
</html>
```